Coffee Roaster Needs A Postcard Design

I am coffee roaster ( a home business) and I would like to create a neighborhood delivery service. Once a month I would delivery fresh roasted coffee to my neighbors. I would like to create a postcard to advertise the coffee delivery service.

Preferences: The postcard would be very simple, primarily black and white ( a little color) with visuals; fresh roasted coffee beans, delivered to the doorstep, a great cup of coffee. Simple steps, 1 2 & 3.

I have a website the postcard advertisement should flow with the site : www.brinmoorcoffeeworks.com

Target Market(s)

Upper class residential neighborhood

Industry/Entity Type

Business

Font styles to use
Serif

Colors
f04a50

Requirements
Must have
• Images _ Coffee Beans

```html
<!DOCTYPE html>
<html lang="en">
<head>
<meta charset="utf-8">
<title>Brinmoor Coffee Works – Postcard</title>
<link rel="stylesheet" href="https://fonts.googleapis.com/css2?family=Cabin+Sketch:wght@400;700&family=Fredoka:wght@600&display=swap">
<style>
  :root {
    --cream: #f4ede1;
    --cream-deep: #eadfcd;
    --ink-brown: #6a4830;
    --bean-dark: #5a3320;
    --bean-mid: #8a5a3a;
    --clay: #b86a3c;
    --steel: #d9d9db;
    --linen: #e6d3b4;
    --leaf: #4f7d2c;
  }
  * { margin: 0; padding: 0; box-sizing: border-box; }
  html, body { width: 1200px; height: 858px; overflow: hidden; background: var(--cream); }
  .postcard {
    position: relative;
    width: 1200px;
    height: 858px;
    background: var(--cream);
    overflow: hidden;
  }
  .photo-beans {
    position: absolute;
    left: 560px; top: 0;
    width: 640px; height: 858px;
    background:
      radial-gradient(ellipse 260px 220px at 380px 420px, var(--bean-dark) 0%, var(--bean-mid) 45%, rgba(184,106,60,0.6) 70%, rgba(184,106,60,0) 100%),
      radial-gradient(ellipse 180px 90px at 470px 720px, rgba(79,125,44,0.75) 0%, rgba(79,125,44,0) 100%),
      linear-gradient(180deg, #eeeeef 0%, var(--steel) 35%, var(--linen) 75%, #d8c09a 100%);
  }
  .pattern-circles {
    position: absolute;
    left: 340px; top: 0;
    width: 520px; height: 858px;
    background: linear-gradient(90deg, rgba(244,237,225,0) 0%, rgba(201,168,132,0.45) 45%, rgba(244,237,225,0) 100%);
  }
  .headline {
    position: absolute;
    left: 40px;
    font-family: "Cabin Sketch", "Comic Sans MS", cursive;
    font-weight: 700;
    color: var(--ink-brown);
    text-transform: uppercase;
    line-height: 1;
    white-space: nowrap;
  }
  .headline--small { font-size: 58px; letter-spacing: 3px; }
  .headline--large { font-size: 128px; letter-spacing: 4px; }
  .headline--medium { font-size: 60px; letter-spacing: 3px; }
  .line-fresh { top: 110px; }
  .line-roasted { top: 190px; }
  .line-coffee { top: 282px; }
  .line-beans { top: 412px; }
  .line-delivered { top: 545px; }
  .line-doorstep { top: 637px; }
  .website {
    position: absolute;
    left: 56px; top: 782px;
    font-family: "Fredoka", "Arial Rounded MT Bold", sans-serif;
    font-weight: 600;
    font-size: 32px;
    letter-spacing: 1px;
    color: var(--bean-dark);
    text-transform: uppercase;
    white-space: nowrap;
  }
</style>
</head>
<body>
  <main class="postcard">
    <div class="photo-beans" role="img" aria-label="Photograph of roasted coffee beans heaped in clay bowls on burlap, with a green coffee leaf and a moka pot behind"></div>
    <div class="pattern-circles" role="img" aria-label="Decorative pattern of scattered brown and beige circles"></div>

    <h1>
      <span class="headline headline--small line-fresh">Fresh</span>
      <span class="headline headline--small line-roasted">Roasted</span>
      <span class="headline headline--large line-coffee">Coffee</span>
      <span class="headline headline--large line-beans">Beans</span>
      <span class="headline headline--medium line-delivered">Delivered to</span>
      <span class="headline headline--medium line-doorstep">the Doorstep</span>
    </h1>

    <p class="website">www.brinmoorcoffeeworks.com</p>
  </main>
</body>
</html>
```